Corlin Network Guild - Original design for WordPress

The requirement is to develop a custom Wordpress theme.
The content and structure section of the brief is provided as a guide for what visual elements need to be addressed in the theme.
Project is to create an original website design and deliver as a WordPress theme to the client.
About the client
CNG is a not-for-profit organisation founded in 1995 to support and represent the interests of the internet community in Western Australia.
Project Vision
We are looking for a clean and modern web design that befits our technical organisation and members.
Members of the public should be able to visit our website and quickly and easily find what they're looking for - so there is an emphasis on readability.
Given our technical audience, we expect a large number of page views will come from mobile devices - so a responsive layout is essential.
Update May 21 Budget has been added to this project for Coding.
Industry/Entity Type
Internet
Coding
Coded - Design and coding required
Number of Pages Required
3 page
Font styles to use
Requirements
Must have
- A detailed brief is provided which is essential reading and should answer any questions.
- Social Media Accounts: Apologies for the poor wording on this requirement, we'd like icon graphics for Friendlio and Chirpet styled appropriately somewhere on the main page.
- We want the best possible outcome, and are keen to discuss any suggestions or clarifications you may have through this process.
Nice to have
- We would prefer backgrounds with a light coloured background, as this gives the site a more modern aesthetic.
- Pictures of Australia are great, but we're primarily based in Perth, Western Australia - so photos of there are much more appropriate for us than Sydney.

```html
<!DOCTYPE html>
<html lang="en">
<head>
<meta charset="utf-8">
<title>Corlin Network Guild</title>
<link href="https://fonts.googleapis.com/css2?family=Open+Sans:wght@300;400;600;700&display=swap" rel="stylesheet">
<style>
:root{
  --header:#2b2b2b;
  --green-1:#0b4a2a;
  --green-2:#0d5a32;
  --green-3:#0f6a3b;
  --orange:#e8892b;
  --ink:#333333;
  --body:#6a6a6a;
  --footer:#3a3a3a;
  --footer-bar:#2e2e2e;
  --footer-text:#a9a9a9;
  --white:#ffffff;
}
*{margin:0;padding:0;box-sizing:border-box}
html,body{width:686px;height:1200px;overflow:hidden;background:var(--white)}
body{position:relative;font-family:"Open Sans",sans-serif;color:var(--ink)}
.abs{position:absolute}
.site-header{left:0;top:0;width:686px;height:45px;background:var(--header)}
.main-nav{right:56px;top:0;height:45px;display:flex;align-items:center;gap:27px;font-size:6.5px;color:var(--white);letter-spacing:.2px}
.brand{left:58px;top:6px;width:120px;height:120px;border-radius:50%;background:var(--header);border:4px solid #e8e8e8;display:flex;align-items:center;justify-content:center;text-align:center;z-index:3;box-shadow:0 2px 6px rgba(0,0,0,.4)}
.brand-name{font-weight:700;font-size:11px;line-height:14px;color:var(--white);letter-spacing:.5px}
.hero{left:0;top:45px;width:686px;height:261px;background:linear-gradient(180deg,#6f7f8c 0%,#8e9aa2 30%,#4b5a66 58%,#2c3c4a 78%,#1f2d38 100%)}
.hero-title{left:0;top:130px;width:686px;text-align:center;color:var(--white);font-size:16px;font-weight:700;letter-spacing:.3px}
.hero-sub{left:0;top:153px;width:686px;text-align:center;color:var(--white);font-size:16px;font-weight:300;letter-spacing:.3px}
.hero-btn{left:289px;top:183px;width:102px;height:27px;background:var(--orange);color:var(--white);font-size:7px;font-weight:700;display:flex;align-items:center;justify-content:center;border-radius:2px}
.hero-arrow{top:162px;width:12px;height:12px;border-radius:50%;background:rgba(255,255,255,.15)}
.features{left:57px;top:262px;width:572px;height:84px;display:flex;box-shadow:0 10px 14px -6px rgba(0,0,0,.35)}
.feature{flex:1;display:flex;padding:14px 12px 0 15px;gap:10px;color:var(--white)}
.feature:nth-child(1){background:var(--green-1)}
.feature:nth-child(2){background:var(--green-2)}
.feature:nth-child(3){background:var(--green-3)}
.feature svg{flex:none;margin-top:4px}
.feature h3{font-size:9px;font-weight:700;margin-bottom:4px}
.feature p{font-size:5.8px;line-height:12px}
.section-title{left:0;width:686px;text-align:center;font-weight:700;font-size:12px;color:var(--ink)}
.section-sub{left:0;width:686px;text-align:center;font-weight:300;font-size:12px;color:var(--ink)}
.section-text{left:115px;width:456px;text-align:center;font-size:6px;line-height:14px;color:var(--body)}
.post-image{width:182px;height:115px}
.post-title{width:182px;font-size:7px;font-weight:700;line-height:13px;color:var(--ink)}
.post-teaser{background:var(--green-1);color:var(--white);padding:26px 15px 0 15px;font-size:6px;line-height:12.5px}
.post-teaser em{display:block;margin-top:4px;font-style:italic}
.about-title{left:277px;top:902px;font-size:12px;font-weight:700}
.about-text{left:277px;width:352px;font-size:6px;line-height:13px;color:var(--body)}
.site-footer{left:0;top:1053px;width:686px;height:119px;background:var(--footer)}
.footer-col{top:1074px;color:var(--footer-text);font-size:6px;line-height:12.8px}
.footer-col h4{color:var(--white);font-size:8px;font-weight:700;margin-bottom:6px}
.footer-col b{color:var(--white);font-weight:700}
.footer-links{display:grid;grid-template-columns:74px 60px}
.footer-bar{left:0;top:1172px;width:686px;height:28px;background:var(--footer-bar);color:var(--footer-text);font-size:6px}
.social{right:57px;top:0;height:28px;display:flex;align-items:center;gap:11px}
.social span.dot{width:7px;height:7px;border-radius:50%;background:var(--footer-text)}
</style>
</head>
<body>

<header>
  <div class="abs site-header"></div>
  <div class="abs brand"><span class="brand-name">CORLIN<br>NETWORK<br>GUILD</span></div>
  <nav class="abs main-nav">
    <span>NEWS</span><span>EVENTS</span><span>ABOUT US</span><span>MEMBERSHIP</span><span>RESOURCES</span><span>MEDIA</span><span>CONTATC US</span>
  </nav>
</header>

<section>
  <div class="abs hero" role="img" aria-label="Photo of a harbour city skyline under a cloudy sky"></div>
  <div class="abs hero-arrow" style="left:24px"></div>
  <div class="abs hero-arrow" style="left:647px"></div>
  <div class="abs hero-title">CNG IS A NOT-FOR-PROFIT ORGANISATION</div>
  <div class="abs hero-sub">FOUNDED IN 1995</div>
  <div class="abs hero-btn">VIEW OUR STORY</div>
</section>

<section class="abs features">
  <div class="feature">
    <svg width="20" height="18" viewBox="0 0 20 18" fill="none" stroke="#fff" stroke-width="1.6"><rect x="1" y="3" width="13" height="13" rx="2"/><path d="M7 11l1-3 9-8 2 2-9 8z" fill="#0b4a2a"/></svg>
    <div><h3>MEMBERS PORTAL</h3><p>Lorem Ipsum is simply dummy text of the printing and typesetting industry Lorem Ipsum is simply dummy...</p></div>
  </div>
  <div class="feature">
    <svg width="22" height="18" viewBox="0 0 22 18" fill="#fff"><circle cx="11" cy="4" r="3.3"/><circle cx="4.5" cy="6" r="2.5"/><circle cx="17.5" cy="6" r="2.5"/><path d="M5 18c0-5 2.5-8 6-8s6 3 6 8z"/><path d="M0 16c0-4 1.8-6 4.5-6 1 0 1.8.3 2.4.8C5.6 12.3 5 14 5 16z"/><path d="M22 16c0-4-1.8-6-4.5-6-1 0-1.8.3-2.4.8 1.3 1.5 1.9 3.2 1.9 5.2z"/></svg>
    <div><h3>SOCIAL MEDIA ACCOUNTS</h3><p>Lorem Ipsum is simply dummy text of the printing and typesetting industry. Lorem Ipsum has been the industry's...</p></div>
  </div>
  <div class="feature">
    <svg width="34" height="20" viewBox="0 0 34 20" fill="#fff"><path d="M0 4l7-3 4 8-7 3z"/><path d="M34 4l-7-3-4 8 7 3z"/><path d="M9 4l6-1 5 2 5-1 2 5-4 6-5 3-6-4-4-3z"/></svg>
    <div><h3>MEMBER BENEFITS</h3><p>Lorem Ipsum is simply dummy text of the printing and typesetting industry. Lorem Ipsum has been the industry's...</p></div>
  </div>
</section>

<section>
  <h2 class="abs section-title" style="top:377px">WELCOME TO CNG</h2>
  <div class="abs section-sub" style="top:396px">CORLIN NETWORK GUILD</div>
  <p class="abs section-text" style="top:419px">The Corlin Network Guild (Inc.) is an organisation that was formed in 1995 to represent the Internet community in Western Australia. At the time of formation, pending regulation and uncertainty meant that collaboration between different businesses in the Internet industry was a necessity.</p>
</section>

<section>
  <h2 class="abs section-title" style="top:484px">RECENT POSTS</h2>
  <p class="abs section-text" style="top:503px;left:60px;width:566px">Lorem Ipsum is simply dummy text of the printing and typesetting industry. Lorem Ipsum has been the industry's standard dummy text ever since</p>

  <div class="abs post-image post-teaser" style="left:57px;top:540px">The Mandatory Data Retention Bill has been the topic of many conversations in our industry over the past months, with the Bill being passed by both houses of Parliament on 26 March 2015...<em>by marion on Wed, 29/04/2015 - 10:47am</em></div>
  <div class="abs post-image" style="left:252px;top:540px;background:linear-gradient(180deg,#1d6f9a,#8fc6de 60%,#dfe9ee)" role="img" aria-label="Photo of a figure walking between server racks into clouds"></div>
  <div class="abs post-image" style="left:447px;top:540px;background:linear-gradient(90deg,#3e5a73,#c9d3da 60%,#e9edf0)" role="img" aria-label="Photo of a technician working at a server rack"></div>
  <div class="abs post-title" style="left:57px;top:663px">REQUEST FOR MEMBER SUBMISSIONS ON DATA RETENTION FAQ</div>
  <div class="abs post-title" style="left:252px;top:663px">REQUEST FOR MEMBER SUBMISSIONS ON DATA RETENTION FAQ</div>
  <div class="abs post-title" style="left:447px;top:664px">REQUEST FOR MEMBER SUBMISSIONS ON DATA RETENTION FAQ</div>

  <div class="abs post-image" style="left:57px;top:707px;background:linear-gradient(135deg,#1a2330,#3f5b78 55%,#111821)" role="img" aria-label="Close-up photo of server hardware with blue lights"></div>
  <div class="abs post-image" style="left:252px;top:707px;background:linear-gradient(135deg,#d9dde0,#8aa9c4 55%,#3d5e80)" role="img" aria-label="Photo of hands typing on a laptop keyboard"></div>
  <div class="abs post-image" style="left:447px;top:708px;background:linear-gradient(180deg,#9a9a9a,#4d4d4d 50%,#2b2b2b)" role="img" aria-label="Photo of a business team with two people shaking hands"></div>
  <div class="abs post-title" style="left:57px;top:830px">REQUEST FOR MEMBER SUBMISSIONS ON DATA RETENTION FAQ</div>
  <div class="abs post-title" style="left:252px;top:830px">REQUEST FOR MEMBER SUBMISSIONS ON DATA RETENTION FAQ</div>
  <div class="abs post-title" style="left:447px;top:831px">REQUEST FOR MEMBER SUBMISSIONS ON DATA RETENTION FAQ</div>
</section>

<section>
  <div class="abs" style="left:57px;top:904px;width:183px;height:107px;background:linear-gradient(135deg,#eef1f3,#c7ced4 55%,#f4f5f6)" role="img" aria-label="Photo of two colleagues reviewing work on a computer monitor"></div>
  <h2 class="abs about-title">ABOUT CNG</h2>
  <p class="abs about-text" style="top:925px">The Corlin Network Guild (Inc.) is an organisation that was formed in 1995 to represent the Internet community in Western Australia. At the time of formation, pending regulation and uncertainty meant that collaboration between different businesses in the Internet industry was a necessity.</p>
  <p class="abs about-text" style="top:976px">Since then, CNG has helped the industry to continue to grow in WA. Leading many vital debates and helping to set policy at different levels, CNG has been instrumental in providing an innovative range of services to association members.</p>
</section>

<footer>
  <div class="abs site-footer"></div>
  <div class="abs footer-col" style="left:57px">
    <h4>WELCOME</h4>
    <div class="footer-links"><span>Home</span><span>Events</span><span>About CNG</span><span>Resources</span><span>News</span><span>&nbsp;Contact</span><span>Peering Exchange</span><span></span><span>Membership</span></div>
  </div>
  <div class="abs footer-col" style="left:198px;width:115px">
    <h4>JOIN US</h4>
    <p>We are looking to increase our membership base. <b>Click here</b> to find out how you can join.</p>
  </div>
  <div class="abs footer-col" style="left:344px;width:125px">
    <h4>OUR MEMBERS</h4>
    <p>CNG currently has three types of membership. Here is a list of our <b>current members.</b></p>
  </div>
  <div class="abs footer-col" style="left:508px;width:125px">
    <h4>GET IN TOUCH</h4>
    <p>Got a question for us? Would you like to know more? Fill out our <b>contact form</b> and we will be straight in touch.</p>
  </div>
  <div class="abs footer-bar">
    <span class="abs" style="left:57px;top:9px">© Copyright 2015 - CNG - All rights reserved</span>
    <div class="abs social">
      <span>Connect with our social network :</span>
      <span class="dot" aria-label="Friendlio"></span><span class="dot" aria-label="Chirpet"></span><span class="dot"></span><span class="dot"></span><span class="dot"></span>
    </div>
  </div>
</footer>

</body>
</html>
```